Business Card/ Banner/ Logo/ Shirt design for (Harbour total Health Club) already have a rough idea

Hi,

I designed the business Harbour Wellness Studio to create an environment where people could walk in to and feel at home, a place they could love and talk to all their friends about. I run group classes, personal training and gym activities however my interaction with clients is on a much deeper level and I help them with inspiration and life coaching improving their life with a holistic approach. I want harbour to become global and be seen as the benchmark for professionalism, yet compassion, wellness and an ora of unconditional love and care for its clients and members. I created Harbour so that people could experience life, energy and passion and begin to really love, enjoy, thrive, create and embrace their dreams and follow them.

I have made a logo that I feel best captures this mission however I used it using Microsoft word and paint so in terms of using it as a template the resolution could become distorted.

So I really reach out to the designers that want to be part of something passionate and help the harbour logo, design and vision come to physical form.

I like the logo I have created and I like purple as a feature colour, however I am open to any alterations or tweaks that your designer prowess may feel that will fit with the mission, description and vision the Harbour Wellness Studio will carry of to invigorate the lives of millions.

I am also looking for a shirt design that looks professional and modern as well as fresh with life and credibility

I appreciate your time, thank you and I would love to have your inspired ideas come to life :)

Regards Tomas

If you need to contact me

Email tomasbrennick@mailvale.net
Mob 0477 213 496

Industry/Entity Type

Life Coaching

Contact Information for Business Card

Harbour Wellness Studio, fitness studio and wellness centre

Logo styles of interest
Emblem Logo
Pictorial/Combination Logo
Abstract Logo
Character Logo
Wordmark Logo
Lettermark Logo
Requirements
Nice to have
• Purple, original "H" logo
Tag line "The heart of vitality"

```html
<!DOCTYPE html>
<html lang="en">
<head>
<meta charset="utf-8">
<title>Harbour Wellness Studio – Business Card</title>
<link rel="stylesheet" href="https://fonts.googleapis.com/css2?family=Montserrat:wght@800&family=Open+Sans:wght@600;700&display=swap">
<style>
  :root {
    --page-bg: #ecebe6;
    --card-cyan: #5fdcf5;
    --ribbon-blue: #3f63f2;
    --brand-purple: #3b2fb5;
    --ink: #111111;
    --name-grey: #d9dee4;
  }
  html, body {
    margin: 0;
    width: 1200px;
    height: 1000px;
    overflow: hidden;
    background: var(--page-bg);
  }
  .business-card {
    position: absolute;
    left: 75px;
    top: 200px;
    width: 1050px;
    height: 600px;
    overflow: hidden;
    box-shadow: 0 10px 30px rgba(0,0,0,0.18);
  }
  .card-pattern-fill {
    position: absolute;
    inset: 0;
    background: linear-gradient(135deg, #7fe6fa 0%, var(--card-cyan) 55%, #4fd2ef 100%);
  }
  .card-ribbons {
    position: absolute;
    inset: 0;
  }
  .brand-block {
    position: absolute;
    left: 540px;
    top: 110px;
    width: 480px;
  }
  .brand-name {
    display: flex;
    align-items: center;
    gap: 14px;
    white-space: nowrap;
    font-family: "Open Sans", sans-serif;
    font-weight: 600;
    font-size: 32px;
    color: var(--brand-purple);
    line-height: 1.1;
  }
  .brand-square {
    width: 36px;
    height: 36px;
    background: var(--brand-purple);
    flex: none;
  }
  .brand-tagline {
    margin-top: 12px;
    padding-left: 50px;
    white-space: nowrap;
    font-family: "Open Sans", sans-serif;
    font-weight: 700;
    font-size: 17px;
    letter-spacing: 3px;
    text-transform: uppercase;
    color: var(--brand-purple);
  }
  .contact-list {
    position: absolute;
    left: 690px;
    top: 300px;
    font-family: "Open Sans", sans-serif;
    font-weight: 700;
    font-size: 19px;
    color: var(--ink);
  }
  .contact-item {
    display: flex;
    align-items: center;
    gap: 12px;
    margin-bottom: 22px;
    white-space: nowrap;
  }
  .contact-icon { width: 22px; height: 22px; flex: none; }
  .person-name {
    position: absolute;
    left: 150px;
    top: 395px;
    font-family: "Montserrat", sans-serif;
    font-weight: 800;
    font-size: 44px;
    font-variant: small-caps;
    color: var(--ink);
    letter-spacing: 1px;
  }
  .person-name .surname {
    color: var(--name-grey);
    -webkit-text-stroke: 1px #444;
  }
  .address-list {
    position: absolute;
    left: 175px;
    top: 470px;
    font-family: "Open Sans", sans-serif;
    font-weight: 700;
    font-size: 19px;
    color: var(--ink);
  }
</style>
</head>
<body>
  <div class="business-card">
    <div class="card-pattern-fill" role="img" aria-label="Light cyan woven check pattern background"></div>

    <svg class="card-ribbons" viewBox="0 0 1050 600" aria-hidden="true">
      <defs>
        <linearGradient id="leafGrad" x1="0" y1="0" x2="1" y2="1">
          <stop offset="0" stop-color="#b4d2ff"/>
          <stop offset="1" stop-color="#4a6cf2"/>
        </linearGradient>
        <linearGradient id="cornerGrad" x1="0" y1="0" x2="1" y2="1">
          <stop offset="0" stop-color="#4f78ff"/>
          <stop offset="1" stop-color="#3352e8"/>
        </linearGradient>
        <linearGradient id="ribbonGrad" x1="0" y1="0" x2="0" y2="1">
          <stop offset="0" stop-color="#9dc2ff"/>
          <stop offset="1" stop-color="#3f63f2"/>
        </linearGradient>
      </defs>
      <path d="M0 250 C 160 230, 330 420, 470 600 L 0 600 Z" fill="url(#leafGrad)"/>
      <path d="M1050 160 C 960 300, 860 480, 720 600 L 1050 600 Z" fill="url(#cornerGrad)"/>
      <path d="M0 575 C 300 570, 700 560, 1050 540 L 1050 600 L 0 600 Z" fill="#3f63f2"/>
      <path d="M770 0 C 640 160, 580 420, 310 600 L 370 600 C 630 430, 680 170, 820 0 Z" fill="url(#ribbonGrad)" stroke="#2d8fa8" stroke-width="1.5"/>
    </svg>

    <div class="brand-block">
      <div class="brand-name"><span class="brand-square"></span>Harbour Wellness Studio</div>
      <div class="brand-tagline">The heart of vitality</div>
    </div>

    <div class="contact-list">
      <div class="contact-item">
        <svg class="contact-icon" viewBox="0 0 24 24"><circle cx="12" cy="12" r="4" fill="none" stroke="#111" stroke-width="2.5"/><path d="M16 8v5a3 3 0 0 0 6 0v-1a10 10 0 1 0-4 8" fill="none" stroke="#111" stroke-width="2.5"/></svg>
        <span>tomasbrennick@mailvale.net</span>
      </div>
      <div class="contact-item">
        <svg class="contact-icon" viewBox="0 0 24 24"><rect x="6" y="2" width="12" height="20" rx="2" fill="none" stroke="#111" stroke-width="2.5"/><line x1="10" y1="18" x2="14" y2="18" stroke="#111" stroke-width="2"/></svg>
        <span>0477 213 496</span>
      </div>
    </div>

    <div class="person-name">Your <span class="surname">Name</span></div>

    <div class="address-list">
      <div class="contact-item">
        <svg class="contact-icon" viewBox="0 0 24 24"><path d="M12 22s7-7 7-12a7 7 0 0 0-14 0c0 5 7 12 7 12z" fill="none" stroke="#111" stroke-width="2.5"/><circle cx="12" cy="10" r="2.5" fill="none" stroke="#111" stroke-width="2"/></svg>
        <span>Address 1</span>
      </div>
      <div class="contact-item">
        <svg class="contact-icon" viewBox="0 0 24 24"><path d="M12 22s7-7 7-12a7 7 0 0 0-14 0c0 5 7 12 7 12z" fill="none" stroke="#111" stroke-width="2.5"/><circle cx="12" cy="10" r="2.5" fill="none" stroke="#111" stroke-width="2"/></svg>
        <span>Address 2</span>
      </div>
    </div>
  </div>
</body>
</html>
```